Medical equipment business looking for professional, unique business card

We need a business card design for a durable medical equipment company. We are small but would like our cards to express that we are much bigger. We focus on braces (back, knee, wrist, etc) but also do crutches, rollators, wheelchairs- basically medical equipment that gets you going and back in Action. Our colors are blue and green and our logo has an arrow and use of a "spine". We'd like to express professionalism while being unique.

Industry/Entity Type

Medical Equipment

Contact Information for Business Card

Professional feel but unique. Memorable.

Font styles to use
Serif
Sans Serif
Other font styles liked:
• verdana

Requirements
Must have
• card holders cell#, business phone#, fax#, email, website address, business address, logo
Nice to have
• use of medical/healthcare related descriptive words, items, look
Should not have
• the wrong colors or cartoon characters.

```html
<!DOCTYPE html>
<html lang="en">
<head>
<meta charset="utf-8">
<title>Kelvane Medical – Business Card</title>
<link href="https://fonts.googleapis.com/css2?family=Open+Sans:wght@400;700&family=Roboto+Condensed:wght@400&display=swap" rel="stylesheet">
<style>
  :root {
    --navy: #00466b;
    --name-blue: #004a70;
    --green: #8dc63f;
    --sky: #0a7bb5;
    --paper: #ffffff;
    --backdrop: #e9e9e9;
    --band-text: #ffffff;
  }
  * { margin: 0; padding: 0; box-sizing: border-box; }
  html, body {
    width: 1200px;
    height: 777px;
    overflow: hidden;
    background: var(--backdrop);
  }
  .business-card {
    position: absolute;
    left: 50px;
    top: 76px;
    width: 1100px;
    height: 624px;
    background: var(--paper);
    overflow: hidden;
  }
  .brand {
    position: absolute;
    left: 90px;
    top: 100px;
    display: flex;
    align-items: center;
    gap: 14px;
    font-family: "Open Sans", Verdana, sans-serif;
    font-weight: 700;
    font-size: 38px;
    color: var(--navy);
    letter-spacing: -0.5px;
  }
  .brand-dot {
    width: 22px;
    height: 22px;
    border-radius: 50%;
    background: var(--green);
  }
  .brand-motif {
    position: absolute;
    left: 494px;
    top: 100px;
    width: 104px;
    height: 306px;
    border-radius: 52px;
    background: linear-gradient(160deg, rgba(10,123,181,0.18), rgba(141,198,63,0.24));
  }
  .holder {
    position: absolute;
    right: 82px;
    top: 100px;
    text-align: right;
    font-family: "Open Sans", Verdana, sans-serif;
  }
  .holder-name {
    font-weight: 700;
    font-size: 52px;
    line-height: 1.05;
    color: var(--name-blue);
    letter-spacing: -0.3px;
  }
  .holder-title {
    margin-top: 2px;
    font-weight: 400;
    font-size: 21px;
    letter-spacing: 12.2px;
    margin-right: -12.2px;
    color: var(--name-blue);
  }
  .contact-band {
    position: absolute;
    left: 0;
    top: 0;
    width: 1100px;
    height: 624px;
  }
  .contact {
    position: absolute;
    top: 512px;
    font-family: "Roboto Condensed", "Arial Narrow", sans-serif;
    font-size: 30px;
    line-height: 36px;
    color: var(--band-text);
  }
  .contact-address { left: 91px; text-align: center; }
  .contact-phones { left: 455px; }
  .contact-phones .label { display: inline-block; width: 38px; }
  .contact-online { right: 82px; text-align: right; }
</style>
</head>
<body>
  <div class="business-card">
    <svg class="contact-band" viewBox="0 0 1100 624" aria-hidden="true">
      <path fill="var(--navy)" d="M0 430 C120 460 230 478 330 474 C520 468 700 412 900 414 C1000 414 1060 426 1100 436 L1100 624 L0 624 Z"/>
    </svg>

    <div class="brand">
      <span class="brand-dot"></span>
      <span class="brand-name">Kelvane Medical</span>
    </div>

    <div class="brand-motif" role="img" aria-label="Decorative brand motif in blue and green"></div>

    <div class="holder">
      <div class="holder-name">Daniel Hartwell</div>
      <div class="holder-title">MEDICAL ENGINEER</div>
    </div>

    <div class="contact contact-address">
      418 W. Alder Street<br>
      Fresno, CA 93721
    </div>
    <div class="contact contact-phones">
      <span class="label">p.</span>555-014-2290<br>
      <span class="label">f.</span>555-014-2290
    </div>
    <div class="contact contact-online">
      daniel@kelvanemedical.com<br>
      www.kelvanemedical.com
    </div>
  </div>
</body>
</html>
```